Pocketful Nell Launching in New Location

I need a marketing postcard that announces the opening of Pocketful Nell! It should grab the attention of the target market by highlighting the services they could use the most. I want them to look at this postcard and say, "Oh my god, I totally need this!" Pocketful Nell is all about putting time back in the lives of busy working people by taking every day tasks off their "to do" lists.

If using pictures, I'd like a more retro look and feel. Pocketful Nell reminds me of the 50' and 60's. Parents and families juggling multiple tasks at once... see pic examples

Details:
Pocketful Nell open for business in Mercer County starting August 4, 2014. Taking reservations now!

What we can do to save YOU time:
Grocery Shopping
Gift Shopping, wrapping and shipping
General Errands
Travel Arrangements and Event Planning
Project Management and Organization

What YOU can do with the time YOU save:
Spend time with your kids, family and friends
Relax and enjoy life!

Grand Opening special - Buy 2 hours, get 1 free! *****I don't know if I will use this, what do you think?******

```html
<!DOCTYPE html>
<html lang="en">
<head>
<meta charset="utf-8">
<title>Pocketful Nell – Grand Opening Postcard</title>
<link href="https://fonts.googleapis.com/css2?family=Roboto+Condensed:wght@400;700&family=Arimo:wght@700&family=Great+Vibes&display=swap" rel="stylesheet">
<style>
  :root{
    --bg-deep:#232f7e;
    --bg-dark:#15152e;
    --maroon:#7a1034;
    --maroon-dark:#5e0b27;
    --teal:#7fb3b0;
    --teal-light:#9cc6c3;
    --teal-deep:#1f5a6e;
    --teal-rim:#3d7d8c;
    --white:#ffffff;
    --ink:#111111;
    --rule:#555555;
    --header-bg:#a9cdca;
  }
  *{margin:0;padding:0;box-sizing:border-box}
  html,body{width:1200px;height:1000px;overflow:hidden}
  body{
    position:relative;
    background:linear-gradient(120deg,var(--bg-deep) 0%,#1d2460 50%,var(--bg-dark) 100%);
    font-family:"Roboto Condensed",Arial,sans-serif;
  }
  .card{position:absolute;box-shadow:6px 8px 14px rgba(0,0,0,.55)}
  .card-front{
    left:228px;top:5px;width:745px;height:478px;
    background:var(--maroon);
    overflow:hidden;
  }
  .front-face{
    position:absolute;left:10px;top:10px;right:10px;bottom:10px;
    background:radial-gradient(ellipse at 40% 40%,var(--teal-light),var(--teal) 70%);
  }
  .corner-ribbon{
    position:absolute;right:-60px;top:42px;width:300px;height:76px;
    background:var(--maroon-dark);
    transform:rotate(45deg);
    color:var(--white);font-family:"Arimo",Arial,sans-serif;font-weight:700;font-size:11px;line-height:13px;
    text-align:center;padding-top:6px;
  }
  .hero{position:absolute;left:172px;top:18px}
  .tagline{
    position:absolute;left:0;width:725px;top:249px;text-align:center;
    font-family:"Great Vibes",cursive;font-size:15px;line-height:18px;color:var(--maroon);
  }
  .section-head{
    position:absolute;height:28px;background:var(--header-bg);
    border:1px solid var(--maroon);
    color:var(--maroon);font-weight:700;font-size:16px;line-height:26px;text-align:center;
    padding:0 20px;white-space:nowrap;
  }
  .section-head::before,.section-head::after{
    content:"";position:absolute;top:3px;width:14px;height:20px;
    background:repeating-linear-gradient(0deg,var(--rule) 0 1px,transparent 1px 3px);
  }
  .section-head::before{left:2px}
  .section-head::after{right:2px}
  .head-save{left:8px;top:287px;width:274px}
  .head-spend{left:441px;top:287px;width:274px;font-size:14px}
  .service-list{
    position:absolute;left:12px;top:323px;list-style:none;
    color:var(--maroon);font-size:16px;line-height:20.5px;
  }
  .service-list li::before{content:"✓";display:inline-block;width:21px;font-weight:700;font-size:18px}
  .benefit-list{
    position:absolute;right:20px;top:321px;width:290px;list-style:none;
    color:var(--maroon);font-size:16px;line-height:20.5px;text-align:right;
  }
  .benefit-list svg{vertical-align:-2px;margin-right:6px}
  .call{position:absolute;right:20px;top:390px;width:200px;text-align:center;color:var(--maroon)}
  .call-label{font-weight:700;font-size:19px;line-height:20px}
  .phone{font-family:"Arimo",Arial,sans-serif;font-weight:700;font-size:28px;line-height:28px;color:var(--maroon)}
  .email{font-weight:700;font-size:13px;line-height:15px}
  .web{position:absolute;left:35px;top:438px;color:var(--maroon);font-weight:700;font-size:13px;line-height:15px}

  .card-back{left:228px;top:500px;width:745px;height:480px;background:var(--white)}
  .back-panel{
    position:absolute;left:0;top:0;width:320px;height:480px;
    background:var(--maroon);padding:10px;
  }
  .back-face{
    width:100%;height:100%;
    background:radial-gradient(ellipse at 40% 40%,var(--teal-light),var(--teal) 70%);
    position:relative;
  }
  .back-banner{position:absolute;left:10px;top:6px}
  .back-tagline{
    position:absolute;left:0;width:300px;top:45px;text-align:center;
    font-family:"Great Vibes",cursive;font-size:12px;color:var(--maroon);
  }
  .about{
    position:absolute;left:20px;top:78px;width:272px;
    color:var(--maroon);font-size:12.4px;line-height:16.2px;text-align:justify;
  }
  .about p{margin-bottom:16px}
  .special{
    position:absolute;left:30px;top:312px;width:240px;height:68px;
    background:var(--maroon);border:4px double var(--teal-light);outline:2px solid var(--maroon);
    color:var(--white);text-align:center;font-family:"Arimo",Arial,sans-serif;font-weight:700;
    font-size:15px;line-height:20px;padding-top:10px;
  }
  .back-contact{position:absolute;left:0;width:300px;top:392px;text-align:center;color:var(--maroon)}
  .back-contact .call-label{font-size:15px;line-height:18px}
  .back-contact .phone{font-size:26px;line-height:28px}
  .back-contact .email{font-size:12px;line-height:14px}

  .address{
    position:absolute;left:420px;top:26px;width:144px;text-align:center;font-style:normal;
    font-family:Arial,sans-serif;font-weight:700;font-size:11px;line-height:14.7px;color:var(--ink);
  }
  .stamp{
    position:absolute;left:638px;top:15px;width:96px;height:96px;border:2px solid var(--ink);
    font-family:Arial,sans-serif;font-size:7.5px;line-height:11px;text-align:center;padding-top:28px;color:var(--ink);
  }
  .write-lines{position:absolute;left:357px;top:143px;width:358px}
  .write-lines span{display:block;height:33.5px;border-top:1px solid var(--rule)}
</style>
</head>
<body>

<section class="card card-front">
  <div class="front-face">
    <svg class="hero" width="400" height="232" viewBox="0 0 400 232">
      <path d="M20 60 Q20 40 40 40 L110 40 Q200 -10 290 40 L360 40 Q380 40 380 60 L380 170 Q380 190 360 195 L40 195 Q20 190 20 170 Z"
            fill="var(--teal-deep)" stroke="var(--teal-rim)" stroke-width="5"/>
      <rect x="60" y="20" width="280" height="165" rx="18" fill="var(--teal-deep)"
            role="img" aria-label="Illustration of a woman with arms folded surrounded by errand icons: shopping bag, notepad, laptop, utensils, baby and a dish of food"/>
      <path d="M35 195 L55 188 L345 188 L365 195 L355 212 L365 230 L35 230 L45 212 Z" fill="var(--maroon-dark)"/>
      <rect x="70" y="182" width="260" height="46" fill="var(--maroon)" stroke="var(--teal-light)" stroke-width="2"/>
      <text x="200" y="214" text-anchor="middle" font-family="Roboto Condensed, Arial, sans-serif" font-size="26" fill="var(--teal-light)">Pocketful Nell</text>
    </svg>
    <p class="tagline">" We run around so you don't have to! "</p>

    <h2 class="section-head head-save">What we can do to save YOU time:</h2>
    <ul class="service-list">
      <li>Grocery Shopping</li>
      <li>Gift Shopping, wrapping and shipping</li>
      <li>General Errands</li>
      <li>Travel Arrangements and Event Planning</li>
      <li>Project Management and Organization</li>
    </ul>

    <h2 class="section-head head-spend">What YOU can do with the time YOU save:</h2>
    <ul class="benefit-list">
      <li><svg width="16" height="16" viewBox="0 0 16 16"><g fill="none" stroke="var(--maroon)" stroke-width="1.3"><circle cx="8" cy="8" r="3.5"/><path d="M8 1v2M8 13v2M1 8h2M13 8h2M3 3l1.4 1.4M11.6 11.6L13 13M3 13l1.4-1.4M11.6 4.4L13 3"/></g></svg>Spend time with your kids, family and friends.</li>
      <li><svg width="16" height="16" viewBox="0 0 16 16"><g fill="none" stroke="var(--maroon)" stroke-width="1.3"><circle cx="8" cy="8" r="3.5"/><path d="M8 1v2M8 13v2M1 8h2M13 8h2M3 3l1.4 1.4M11.6 11.6L13 13M3 13l1.4-1.4M11.6 4.4L13 3"/></g></svg>Relax and enjoy life!</li>
    </ul>

    <div class="call">
      <p class="call-label">Call now !</p>
      <p class="phone">555-014-227</p>
      <p class="email">nell@pocketfulnell.biz</p>
    </div>
    <p class="web">www.pocketfulnell.biz</p>
  </div>
  <div class="corner-ribbon">Pocketful Nell open for<br>business in Mercer County<br>starting August 4, 2014.<br>Taking reservations now !</div>
</section>

<section class="card card-back">
  <div class="back-panel">
    <div class="back-face">
      <svg class="back-banner" width="280" height="42" viewBox="0 0 280 42">
        <path d="M0 10 L30 10 L30 36 L0 36 L10 23 Z" fill="var(--maroon-dark)"/>
        <path d="M280 10 L250 10 L250 36 L280 36 L270 23 Z" fill="var(--maroon-dark)"/>
        <rect x="22" y="2" width="236" height="36" fill="var(--maroon)" stroke="var(--teal-light)" stroke-width="1.5"/>
        <text x="140" y="28" text-anchor="middle" font-family="Roboto Condensed, Arial, sans-serif" font-size="20" fill="var(--teal-light)">Pocketful Nell</text>
      </svg>
      <p class="back-tagline">" We run around so you don't have to! "</p>
      <div class="about">
        <p>Pocketful Nell is a comprehensive service helping busy people manage their lives more efficiently. By blending the services of a celebrity personal assistant with those of a traditional hotel-based concierge, we allow you to achieve balance in all areas.</p>
        <p>Pocketful Nell offers you one of the most valuable things in the world; time. More time for you to do what you wish – spend time with your family and friends, go to the gym, on vacation or simply relaxing!</p>
        <p>Contact us today and discover how we can help you reclaim your leisure time and rebalance your life.</p>
      </div>
      <div class="special">Grand Opening special<br>Buy 2 hours, get 1 free!</div>
      <div class="back-contact">
        <p class="call-label">Taking reservations now !</p>
        <p class="phone">555-014-227</p>
        <p class="email">nell@pocketfulnell.biz</p>
      </div>
    </div>
  </div>

  <address class="address">Street Adress<br>City<br>State/Province<br>Postal Code<br>Country/Region</address>
  <div class="stamp">PLEASE<br>PLACE<br>STAMP<br>HERE</div>
  <div class="write-lines"><span></span><span></span><span></span><span></span><span></span><span></span><span></span><span></span><span></span></div>
</section>

</body>
</html>
```